Fixing all glass products,fitting security doors,flyscreens,splashbacks,glazing

Looking for perhaps a liitle happy chap carrying a glass panel with crach throught it and maybe the pane of glass 'hurting' so it had 'pain'???
Open to suggestions

Security

Brightway Glazeworks
Dale Morrow
Specialising in security doors,flyscreens,splashbacks
0451736208
dalemorrow418@postvane.com

```html
<!DOCTYPE html>
<html lang="en">
<head>
<meta charset="utf-8">
<title>Brightway Glazeworks – Business Card</title>
<link rel="stylesheet" href="https://fonts.googleapis.com/css2?family=Fredoka:wght@500;600;700&display=swap">
<style>
  :root {
    --ink-dark: #15161d;
    --glass-shade: #2a2d38;
    --glass-light: #8f939c;
    --white: #ffffff;
    --violet: #9d3ff2;
    --bubble: #cfd1d4;
    --black: #000000;
  }
  html, body {
    margin: 0;
    padding: 0;
    overflow: hidden;
    background: var(--ink-dark);
  }
  .card {
    position: relative;
    width: 702px;
    height: 1200px;
    overflow: hidden;
    font-family: "Fredoka", "Arial Rounded MT Bold", sans-serif;
    text-align: center;
  }
  .shattered-backdrop {
    position: absolute;
    inset: 0;
    background:
      radial-gradient(circle at 44px 796px, var(--glass-light) 0, #5a5e68 90px, transparent 420px),
      linear-gradient(160deg, var(--glass-shade) 0%, var(--ink-dark) 55%, #23252e 100%);
  }
  .line {
    position: absolute;
    left: 0;
    width: 100%;
    margin: 0;
    line-height: 1;
  }
  .business-name {
    top: 84px;
    font-size: 52px;
    font-weight: 600;
    color: var(--white);
  }
  .owner-name {
    top: 146px;
    font-size: 72px;
    font-weight: 600;
    color: var(--violet);
  }
  .services {
    top: 224px;
    font-size: 42px;
    font-weight: 600;
    color: var(--white);
    line-height: 66px;
  }
  .ouch-bubble {
    position: absolute;
    left: 0;
    top: 0;
  }
  .phone {
    top: 1018px;
    font-size: 86px;
    font-weight: 600;
    color: var(--violet);
    letter-spacing: 1px;
  }
  .email {
    top: 1097px;
    font-size: 36px;
    font-weight: 600;
    color: var(--violet);
  }
</style>
</head>
<body>
  <main class="card">
    <div class="shattered-backdrop" role="img" aria-label="Dark pane of shattered glass with cracks radiating from an impact point at the lower left"></div>

    <h1 class="line business-name">Brightway Glazeworks</h1>
    <h2 class="line owner-name">Dale Morrow</h2>
    <p class="line services">Specialising in security<br>doors, flyscreens<br>&amp; splash backs</p>

    <svg class="ouch-bubble" width="702" height="1200" viewBox="0 0 702 1200" aria-hidden="true">
      <path fill="var(--bubble)" d="M306 570 C390 570 458 612 458 664 C458 716 390 758 306 758 C292 758 280 757 268 755 L249 797 L238 748 C190 732 154 700 154 664 C154 612 222 570 306 570 Z"/>
      <text x="306" y="686" text-anchor="middle" font-family="Fredoka, sans-serif" font-weight="700" font-size="60" fill="var(--black)">OUCH!</text>
    </svg>

    <p class="line phone">0451736208</p>
    <p class="line email">dalemorrow418@postvane.com</p>
  </main>
</body>
</html>
```